Corvell Ashdown Website

Updated website for Corvell Ashdown Dry Cleaners & Garment Care.

Please look at www.tindalepressers.example we really like this site!!!

We are not set on colors or fonts. Looking for an professional easy to use site that looks and works even better on a mobile device. 90% of our customers visit us on cell phones.

Target Market(s)

We are located in an up scale area with young trendy individuals but, also very successful mature customers as well. Probably geared more to tech savvy younger crowd.

Industry/Entity Type

Dry Cleaning

Coding

Coded - Design and coding required

Font styles to use
Serif
Script

Colors
85abd2
85cae6
cee9f5
cfdeed
757575

Requirements
Must have
• Must look good on a mobile device and have sign up for our pick up and delivery. Geographical pick up and delivery perimeters would be great as well. Capturing emails and other user data for future marketing. We do a lot of advertising.
• Please look at www.tindalepressers.example we really like this site!!!
• Search engine optimized.
• Also we are adding a new POS system that will have a login for customers and possibly an app.
Nice to have
• 100% satisfaction guaranteed and scrolling reviews somewhere on the page.

```html
<!DOCTYPE html>
<html lang="en">
<head>
<meta charset="utf-8">
<title>Corvell Ashdown Dry Cleaners &amp; Garment Care</title>
<link rel="stylesheet" href="https://fonts.googleapis.com/css2?family=Open+Sans:ital,wght@0,300;0,400;0,600;0,700;1,300;1,400&display=swap">
<style>
:root{
  --page:#dbe6f2;
  --panel:#9aabcf;
  --panel-strip:#aab9d7;
  --band:#94a8cc;
  --ink:#2a2a2a;
  --ink-soft:#555;
  --dark:#222325;
  --dark-foot:#252526;
  --white:#fff;
  --black:#0b0b0b;
  --rule:#4a4a4a;
}
*{box-sizing:border-box;margin:0;padding:0}
html,body{width:1200px;height:2748px;overflow:hidden}
body{font-family:"Open Sans",Arial,sans-serif;background:var(--page);color:var(--ink);position:relative}
.abs{position:absolute}

/* hero */
.hero{left:0;top:0;width:1200px;height:467px;background:linear-gradient(180deg,#4f6f98 0%,#8aa3c0 35%,#d9dfe2 62%,#b7a472 78%,#55633c 100%)}
.brand{left:220px;top:30px;color:var(--white);font-weight:600;font-size:16px}
.login{left:888px;top:34px;color:var(--white);font-size:10px;letter-spacing:1px}
.hero-title{left:0;width:1200px;top:88px;text-align:center;color:var(--ink);font-weight:400;font-size:32px}
.hero-sub{left:0;width:1200px;top:136px;text-align:center;color:var(--ink);font-size:20px}
.hero-line{left:0;width:1200px;top:176px;text-align:center;color:var(--ink);font-size:16px}

/* signup panel */
.signup{left:284px;top:366px;width:632px;height:224px;background:var(--panel)}
.signup p{position:absolute;left:30px;right:30px;top:40px;text-align:center;color:var(--white);font-size:13px;line-height:20px}
.btn-black{background:var(--black);color:var(--white);font-size:10px;letter-spacing:1px;text-align:center;border:none;font-family:inherit}
.schedule{left:222px;top:80px;width:188px;height:26px;line-height:26px}
.signup-strip{left:32px;top:132px;width:568px;height:52px;background:var(--panel-strip)}
.email{left:50px;top:10px;width:343px;height:30px;background:var(--white);color:#888;font-size:11px;text-align:center;line-height:30px}
.join{left:404px;top:10px;width:114px;height:30px;line-height:30px;font-size:11px}

/* steps */
.step{top:680px;width:193px;height:188px;overflow:hidden}
.step-caption{position:absolute;left:0;right:0;bottom:0;height:34px;background:rgba(20,20,20,.78);color:var(--white);text-align:center;padding-top:4px}
.step-caption b{display:block;font-size:10px;font-weight:600}
.step-caption span{display:block;font-size:8px;line-height:10px}

/* guarantee */
.guarantee{left:0;top:896px;width:1200px;height:124px;background:var(--band)}
.guarantee h2{position:absolute;left:462px;top:20px;color:var(--white);font-size:27px;font-weight:400}
.guarantee p{position:absolute;left:462px;top:58px;width:470px;color:var(--white);font-size:20px;line-height:26px;font-weight:300}

/* services */
.services{left:0;top:1121px;width:1200px;height:698px;background:var(--dark)}
.tile{position:absolute}
.tile span{position:absolute;right:10px;top:28px;color:var(--white);font-size:11px}

/* testimonials */
.reviews-title{left:0;width:1200px;top:1908px;text-align:center;font-size:34px;font-weight:300;color:var(--ink)}
.review{top:1974px;width:370px;text-align:center}
.avatar{width:64px;height:64px;border-radius:50%;margin:0 auto}
.review q{display:block;margin-top:40px;font-style:italic;font-weight:300;font-size:13.5px;line-height:22px;color:var(--ink-soft);quotes:none}
.review .tag{margin-top:30px;font-size:12px;color:var(--ink-soft)}
.review .who{margin-top:12px;font-size:14px;color:var(--ink-soft)}
.dots{left:586px;top:2252px}
.dots i{display:inline-block;width:5px;height:5px;border-radius:50%;background:#333;margin-right:5px}

/* footer */
.footer{left:0;top:2367px;width:1200px;height:381px;background:var(--dark-foot);color:var(--white)}
.hours{left:220px;top:68px;width:231px}
.hours h3{font-size:11px;font-weight:600;margin-bottom:14px}
.hours table{width:100%;border-collapse:collapse;font-size:11px}
.hours td{height:31px;border-top:1px solid var(--rule)}
.hours tr:last-child td{border-bottom:1px solid var(--rule)}
.map{left:476px;top:64px;width:233px;height:255px;background:linear-gradient(160deg,#8c8f94 0%,#6f7a86 45%,#3f5f84 70%,#4d6989 100%)}
.follow{left:747px;top:68px;width:233px}
.follow h3{font-size:9px;letter-spacing:1px;font-weight:600}
.social{display:flex;gap:8px;margin:20px 0 0 32px}
.social i{width:32px;height:32px;border-radius:50%;background:var(--white)}
.links{list-style:none;margin-top:22px}
.links li{font-size:11px;font-weight:600;height:31px;line-height:30px;border-bottom:1px solid var(--rule)}
</style>
</head>
<body>

<header class="abs hero" role="img" aria-label="Photograph of a sunlit autumn tree in misty countryside under a blue sky"></header>
<div class="abs brand">Corvell Ashdown Dry Cleaners</div>
<div class="abs login">LOGIN / SIGN UP</div>
<h1 class="abs hero-title">Save Time, Enjoy Life</h1>
<div class="abs hero-sub">Laundry Day Redefined</div>
<div class="abs hero-line">With Ashdown Dry Cleaning Pick Up and Delivery Service!</div>

<section class="abs signup">
  <p>Choose from wash &amp; fold, dry cleaning, tailoring and more; and easily arrange pickup and delivery with flexible scheduling.</p>
  <div class="abs btn-black schedule">SCHEDULE YOUR PICKUP NOW!</div>
  <div class="abs signup-strip">
    <div class="abs email">E-Mail Address</div>
    <div class="abs btn-black join">JOIN US</div>
  </div>
</section>

<section>
  <div class="abs step" style="left:211px;background:linear-gradient(135deg,#d9d6d3,#8b7560)" role="img" aria-label="Photo of a woman with a laptop beside a dog">
    <div class="step-caption"><b>Place Your Order</b><span>Select your Pick-up &amp; Drop-Off date, time and location</span></div></div>
  <div class="abs step" style="left:407px;background:linear-gradient(160deg,#b8cde6,#c27a3e 55%,#3a3a3a)" role="img" aria-label="Photo of a laundry basket full of clothes">
    <div class="step-caption"><b>We Collect</b><span>We'll come to you and collect your laundry</span></div></div>
  <div class="abs step" style="left:603px;background:linear-gradient(180deg,#3c3c3e,#c9ccd2)" role="img" aria-label="Photo of white shirts on hangers">
    <div class="step-caption"><b>We Clean</b><span>We'll take care of laundry day for you, professionally</span></div></div>
  <div class="abs step" style="left:799px;background:linear-gradient(180deg,#f1f1f1,#cfcfcf)" role="img" aria-label="Photo of a wedding dress hanging by a window">
    <div class="step-caption"><b>We Deliver</b><span>We deliver your fresh clean clothes back to your door</span></div></div>
</section>

<section class="abs guarantee">
  <svg class="abs" style="left:366px;top:8px" width="80" height="108" viewBox="0 0 80 108" aria-hidden="true">
    <path d="M24 60 L12 104 L26 94 L34 106 L40 70 Z M56 60 L68 104 L54 94 L46 106 L40 70 Z" fill="#fff"/>
    <circle cx="40" cy="38" r="36" fill="#fff"/>
    <circle cx="40" cy="38" r="27" fill="none" stroke="#94a8cc" stroke-width="2"/>
    <text x="40" y="45" text-anchor="middle" font-family="Open Sans,Arial,sans-serif" font-size="18" font-weight="700" fill="#94a8cc">100%</text>
  </svg>
  <h2>Satisfaction Guarantee</h2>
  <p>If you're ever unhappy with the quality of our dry cleaning or pressing, we'll redo the item for free</p>
</section>

<section class="abs services">
  <div class="tile" style="left:220px;top:90px;width:174px;height:297px;background:linear-gradient(160deg,#3a3a3a,#6b2d22 60%,#2a2a2a)" role="img" aria-label="Photo of leather jackets"><span>Suede &amp; Leather</span></div>
  <div class="tile" style="left:401px;top:90px;width:246px;height:126px;background:linear-gradient(180deg,#6b5040,#2e3d5c 50%,#cfd6e0)" role="img" aria-label="Photo of shirts on a rack"><span>Shirt Laundering</span></div>
  <div class="tile" style="left:401px;top:224px;width:246px;height:163px;background:linear-gradient(180deg,#d9d3c7,#a69271)" role="img" aria-label="Photo of a couple in wedding attire"><span>Wedding &amp; Formal Gowns</span></div>
  <div class="tile" style="left:654px;top:90px;width:326px;height:189px;background:linear-gradient(135deg,#e6e3e0,#c6a98f 60%,#6a5b52)" role="img" aria-label="Photo of folded knit sweaters"><span>Wash &amp; Fold</span></div>
  <div class="tile" style="left:220px;top:396px;width:174px;height:201px;background:linear-gradient(160deg,#f2f2f2,#6fa9a0)" role="img" aria-label="Photo of hands at a sewing machine"></div>
  <div class="tile" style="left:401px;top:396px;width:246px;height:201px;background:linear-gradient(180deg,#2b2f36,#9ca2aa 60%,#e0e0e0)" role="img" aria-label="Photo of garments in dry cleaning bags"><span>Dry Cleaning</span></div>
  <div class="tile" style="left:654px;top:286px;width:180px;height:311px;background:linear-gradient(160deg,#f4f4f6,#c9cbd3)" role="img" aria-label="Photo of white bedding"></div>
  <div class="tile" style="left:841px;top:286px;width:139px;height:311px;background:linear-gradient(160deg,#7a6f68,#d2a060 55%,#4f7f70)" role="img" aria-label="Photo of a cat lying on a rug"><span>Area Rugs</span></div>
</section>

<h2 class="abs reviews-title">What Our Customers Are Saying</h2>
<div class="abs review" style="left:225px">
  <div class="avatar" style="background:linear-gradient(135deg,#e8c431,#5f7a3c)" role="img" aria-label="Customer portrait"></div>
  <q>Walking into Ashdown is like a breath of fresh air. It is well-designed, clean, and naturally lit. The service team is friendly and helpful and I love, love, love the fact that everything is toxin-free. I'm telling all my friends about this place ... and now you too</q>
  <div class="tag">Breath of Fresh Air</div>
  <div class="who">Maren T</div>
</div>
<div class="abs review" style="left:605px">
  <div class="avatar" style="background:linear-gradient(135deg,#8c8f92,#4a4d50)" role="img" aria-label="Customer portrait"></div>
  <q>I never realized I could get this excited about dry-cleaning. Man, I wish more companies had this level of customer service, sophistication, and eco-awareness. This is how a company should be run!!</q>
  <div class="tag">Actually Excited</div>
  <div class="who">Theo Lund</div>
</div>
<div class="abs dots"><i></i><i></i><i></i></div>

<footer class="abs footer">
  <div class="abs hours">
    <h3>Hours:</h3>
    <table>
      <tr><td>Saturday</td><td>8AM–5PM</td></tr>
      <tr><td>Sunday</td><td>Closed</td></tr>
      <tr><td>Monday</td><td>7AM–7PM</td></tr>
      <tr><td>Tuesday</td><td>7AM–7PM</td></tr>
      <tr><td>Wednesday</td><td>7AM–7PM</td></tr>
      <tr><td>Thursday</td><td>7AM–7PM</td></tr>
      <tr><td>Friday</td><td>7AM–7PM</td></tr>
    </table>
  </div>
  <div class="abs map" role="img" aria-label="Map showing the shop location by the lake"></div>
  <div class="abs follow">
    <h3>FOLLOW US FOR MONTHLY SPECIALS</h3>
    <div class="social"><i></i><i></i><i></i><i></i><i></i></div>
    <ul class="links">
      <li>Home</li><li>Services</li><li>Contact Us</li><li>Pick Up &amp; Delivery</li><li>Login / Sign Up</li>
    </ul>
  </div>
</footer>

</body>
</html>
```